Travel Adventure Challenge Poster/Information Sheet

We have created a corporate incentive travel package we’ve called the “The Quorvex Pursuit Circuit” This is an experiential travel adventure,….not a tour, an adventure designed to awaken the senses, tap into your realm of creativity and resourcefulness, and connect you with a new environment.
“X” for the mystery, as in, “the unknown”
“Challenge” for the competitive element: - each day offers a competitive challenge that calls forth creativity, resourcefulness and team interaction.
“Connection” for the experience of truly relating to the culture that the participant is emerged in.
We require a one-pager (A4) 8.5x11, one-sided informative ad that is directed toward corporate incentive travel clientele and adventure enthusiasts. I've attached 2 logo's One for the event itself and the other for the parent company. (The Quorvex Pursuit Circuit and Bramwell Journey Services) This is a teaser. The goal is to have people contact us by phone, web, or email to find out more information. I've also attached several pages of content and images to choose from...The green, black/grey and white are the standard colors for the logo and we are open to incorporating vibrant complementary colors. Let your creativity flow! We look forward to seeing what you can create!

```html
<!DOCTYPE html>
<html lang="en">
<head>
<meta charset="utf-8">
<title>The Quorvex Pursuit Circuit – Travel Adventure Flyer</title>
<link rel="stylesheet" href="https://fonts.googleapis.com/css2?family=Montserrat:wght@700&family=Open+Sans:wght@400;700&family=PT+Sans+Narrow:wght@400;700&family=PT+Sans:wght@400&display=swap">
<style>
  :root {
    --lime: #84fc04;
    --brand-green: #8be21a;
    --charcoal: #3e4345;
    --ink: #1d1f20;
    --white: #ffffff;
    --slate: #5b6266;
    --blush: #f3a4b0;
  }
  * { box-sizing: border-box; margin: 0; padding: 0; }
  html, body { width: 1200px; height: 1000px; overflow: hidden; }
  body { background: var(--lime); position: relative; font-family: "Open Sans", Arial, sans-serif; }

  .flyer {
    position: absolute; left: 203px; top: 52px;
    width: 710px; height: 853px;
    background: var(--charcoal);
    overflow: hidden;
  }
  .hero { position: absolute; left: 0; top: 0; width: 710px; height: 603px; overflow: hidden; }
  .hero-art { position: absolute; left: 0; top: 0; }

  .event-name {
    position: absolute; left: 0; top: 18px; width: 272px; height: 60px;
    background: var(--white);
    display: flex; align-items: center; gap: 10px; padding-left: 30px;
    font-family: "PT Sans Narrow", Arial, sans-serif; font-weight: 700;
    font-size: 19px; color: var(--charcoal); letter-spacing: .3px;
  }
  .event-name .mark { width: 16px; height: 16px; background: var(--brand-green); flex: none; }

  .tagline {
    position: absolute; left: 200px; top: 82px;
    transform: rotate(56deg); transform-origin: 0 0;
    font-family: "Montserrat", Arial, sans-serif; font-weight: 700;
    font-size: 16px; line-height: 19px; letter-spacing: .5px;
    white-space: nowrap; color: var(--white);
  }
  .tagline .dark { color: var(--ink); }

  .faint-name {
    position: absolute; left: 172px; top: 560px;
    transform: rotate(-56deg); transform-origin: 0 0;
    font-family: "Montserrat", Arial, sans-serif; font-weight: 700;
    font-size: 19px; line-height: 21px; letter-spacing: 1px;
    color: rgba(255,255,255,.4); white-space: nowrap;
  }

  .pillars {
    position: absolute; left: 415px; top: 193px; width: 250px;
    font-family: "PT Sans", Arial, sans-serif; font-size: 12.6px; line-height: 19.5px;
    color: var(--white);
  }
  .pillar { margin-bottom: 16px; }
  .pillar-title {
    font-family: "PT Sans Narrow", Arial, sans-serif;
    font-weight: 700; font-size: 19px; letter-spacing: .3px; margin-right: 4px;
  }
  .arrows { position: absolute; left: 652px; top: 341px; }

  .parent-company {
    position: absolute; left: 372px; top: 540px; width: 338px; height: 63px;
    background: var(--white); display: flex; align-items: center; padding-left: 14px;
    font-family: "PT Sans Narrow", Arial, sans-serif; font-weight: 700;
    font-size: 16px; color: var(--slate); letter-spacing: .4px;
  }

  .promise {
    position: absolute; left: 0; top: 603px; width: 710px; height: 143px;
    background: var(--charcoal); color: var(--white); text-align: center;
    padding-top: 10px;
  }
  .promise p { font-size: 14.4px; line-height: 21px; padding: 0 60px; }
  .promise .offer {
    margin-top: 14px; font-weight: 700; font-size: 20px; line-height: 28px;
    color: var(--brand-green); padding: 0 70px;
  }
  .dates {
    position: absolute; left: 0; top: 746px; width: 710px; height: 44px;
    background: var(--brand-green); color: var(--white); text-align: center;
    font-family: "PT Sans Narrow", Arial, sans-serif; font-size: 29px; line-height: 44px;
  }
  .contact {
    position: absolute; left: 0; top: 790px; width: 710px; height: 63px;
    background: var(--charcoal); color: var(--white); text-align: center;
    font-size: 14.4px; line-height: 20px; padding-top: 9px;
  }
</style>
</head>
<body>
  <main class="flyer">
    <section class="hero">
      <svg class="hero-art" width="710" height="603" viewBox="0 0 710 603">
        <defs>
          <linearGradient id="sprint-tones" x1="0" y1="0" x2="1" y2="1">
            <stop offset="0" stop-color="#b79a9c"/>
            <stop offset=".35" stop-color="#4b4548"/>
            <stop offset=".7" stop-color="#3b3a3e"/>
            <stop offset="1" stop-color="#8a6f72"/>
          </linearGradient>
          <linearGradient id="office-tones" x1="0" y1="0" x2="0" y2="1">
            <stop offset="0" stop-color="#e6e3e2"/><stop offset="1" stop-color="#9a8f8c"/>
          </linearGradient>
          <linearGradient id="beach-tones" x1="0" y1="0" x2="0" y2="1">
            <stop offset="0" stop-color="#9fd6ea"/><stop offset=".6" stop-color="#d7a98c"/><stop offset="1" stop-color="#5fc0c4"/>
          </linearGradient>
          <linearGradient id="snow-tones" x1="0" y1="0" x2="0" y2="1">
            <stop offset="0" stop-color="#7fb6e6"/><stop offset=".6" stop-color="#9aa1b0"/><stop offset="1" stop-color="#eef2f6"/>
          </linearGradient>
        </defs>
        <rect x="0" y="0" width="710" height="603" fill="url(#sprint-tones)" role="img" aria-label="Photo: businessman in a suit crouched in a sprint start on a running track"/>
        <polygon points="380,0 710,0 710,603 520,603 520,160" fill="rgba(40,40,44,.45)"/>
        <polygon points="97,78 237,78 404,343 237,603 97,603" fill="var(--brand-green)"/>
        <polygon points="0,83 97,83 202,273 0,273" fill="url(#office-tones)" role="img" aria-label="Photo: cheering team of office colleagues"/>
        <polygon points="0,276 222,276 265,343 242,418 0,418" fill="url(#beach-tones)" role="img" aria-label="Photo: family celebrating on a tropical beach"/>
        <polygon points="0,421 240,421 128,603 0,603" fill="url(#snow-tones)" role="img" aria-label="Photo: group of snowboarders on a snowy slope"/>
      </svg>

      <div class="event-name"><span class="mark"></span>The Quorvex Pursuit Circuit</div>

      <div class="tagline">
        <div>AN EXPERIENTIAL TRAVEL</div>
        <div>ADVENTURE DESIGNED TO</div>
        <div class="dark">EXPAND THE CREATIVE MIND</div>
      </div>

      <div class="faint-name">
        <div>PURSUIT</div>
        <div>CIRCUIT</div>
      </div>

      <div class="pillars">
        <p class="pillar"><span class="pillar-title">COMPETE</span> Build team and leadership skills while completing daily mystery challenges and win prizes!</p>
        <p class="pillar"><span class="pillar-title">CREATE</span> We’ve designed a cultural playground for the mind to explore its creative pipeline, immersed in the rich cultures of Vietnam and Costa Rica. Experience the local cuisine, language, history and communities. Explore, revive and reset your creative process.</p>
        <p class="pillar"><span class="pillar-title">CONNECT</span> Intimately explore the culture, connect with your team, the community, and the experience of yourself in a vibrant setting.</p>
      </div>

      <svg class="arrows" width="56" height="14" viewBox="0 0 56 14" aria-hidden="true">
        <g fill="var(--blush)">
          <polygon points="0,7 8,1 8,13"/><polygon points="10,7 18,1 18,13"/>
          <polygon points="20,7 28,1 28,13"/><polygon points="30,7 38,1 38,13"/>
          <polygon points="40,7 48,1 48,13"/>
        </g>
      </svg>

      <div class="parent-company">Bramwell Journey Services</div>
    </section>

    <section class="promise">
      <p>Your Quorvex team is on the ground beside you ensuring that each element of the event is managed to perfection. We promise that when the daily challenge is complete, luxurious accommodation and relaxation are waiting!</p>
      <p class="offer">Experience a 5* - 10 day mystery challenge immersed in the vibrancy of Vietnam or Costa Rica.</p>
    </section>

    <section class="dates">Vietnam October 2014 Costa Rica November 2014</section>

    <section class="contact">
      <p>Contact us to learn more. hello@bramwelljourney.example 1.800.555.0147 x 210</p>
      <p>www.quorvexpursuit.example</p>
    </section>
  </main>
</body>
</html>
```